We also do Plumbing Reminder! Our Primary Color is Green with Gold accent.

We are a HVAC, plumbing, and Controls contractor based out of West Michigan, Serving the entire west side of the state.
We want to remind our customers we do plumbing. Customers don't know or remember that we do plumbing. We would like the final design to show images, and descriptions of plumbing services we offer.

Lift Stations
Sinks
Confined Space
Backflow Prevention Devices​ (testing, installation, & service)
Drinking Fountains
Roof Drains
Sump Pumps
Water Main Emergency Service
Toilets / Urinals
Faucets / Shower Valves
Piping​ (copper, PVC, steel, PEX, galvanized)
Water Heaters
Floor and Sink Drains
​NEW INSTALLATIONS, SERVICE, AND MAINTENANCE OF ALL BRANDS OF EQUIPMENT

```html
<!DOCTYPE html>
<html lang="en">
<head>
<meta charset="UTF-8">
<title>Harlow Mechanical – Plumbing Services Flyer</title>
<link href="https://fonts.googleapis.com/css2?family=Poppins:wght@400;500;600;700;800;900&display=swap" rel="stylesheet">
<style>
  :root{
    --green:#0b6b45;
    --gold:#d4b45c;
    --ink:#141414;
    --text:#222;
    --paper:#ffffff;
    --backdrop:#f1f1f1;
  }
  *{box-sizing:border-box;margin:0;padding:0}
  html,body{width:783px;height:1200px;overflow:hidden;background:var(--backdrop);font-family:'Poppins',sans-serif}
  .canvas{position:relative;width:783px;height:1200px}
  .flyer{position:absolute;left:4px;top:100px;width:775px;height:1000px;background:var(--paper);overflow:hidden;box-shadow:0 2px 8px rgba(0,0,0,.12)}
  .hero-art{position:absolute;left:0;top:0}
  .brand{position:absolute;left:40px;top:40px;display:flex;align-items:center;gap:10px;color:var(--green);font-weight:800;font-size:22px;line-height:1;letter-spacing:.5px}
  .brand-dot{width:26px;height:26px;border-radius:50%;background:var(--green)}
  .headline{position:absolute;left:39px;top:140px;color:var(--green);font-weight:800;line-height:.92}
  .headline .l1{font-size:48px;display:block}
  .headline .l2{font-size:58px;display:block}
  .headline .sub{display:block;font-size:20px;color:var(--ink);font-weight:700;margin-top:4px;letter-spacing:.2px}
  .intro{position:absolute;left:40px;top:281px;width:360px;color:#fff;font-size:13.5px;font-weight:600;line-height:1.25}
  .attention{position:absolute;left:38px;top:361px;width:290px;height:38px;background:var(--gold);border-radius:0 20px 20px 0}
  .attention .badge{position:absolute;left:0;top:0;width:38px;height:38px;border-radius:50%;background:var(--green);display:flex;align-items:center;justify-content:center;border:2px solid #fff}
  .attention .word{position:absolute;left:62px;top:0;line-height:40px;font-size:29px;font-weight:800;color:var(--ink)}
  .lead{position:absolute;left:42px;top:413px;font-size:16px;font-weight:700;color:var(--ink)}
  .lead em{font-style:normal;color:var(--gold)}
  .service{position:absolute;display:flex;align-items:center;gap:10px;width:240px}
  .thumb{flex:none;width:62px;height:62px;border-radius:50%;border:4px solid var(--gold);padding:2px;background:#fff}
  .thumb.g{border-color:var(--green)}
  .thumb i{display:block;width:100%;height:100%;border-radius:50%}
  .service h3{font-size:12.5px;font-weight:700;color:var(--green);line-height:1.05;text-transform:uppercase}
  .service h3 span{color:var(--gold)}
  .service small{display:block;font-size:10px;color:var(--text);line-height:1.15;margin-top:1px}
  .service p{font-size:12.5px;color:var(--text);line-height:1.1;margin-top:2px}
  .offer{position:absolute;left:500px;top:457px;width:275px;height:203px;background:var(--green);border-radius:18px 0 0 0}
  .offer li{position:absolute;left:52px;list-style:none;color:#fff;font-size:17px;font-weight:700;line-height:1.15}
  .offer-icon{position:absolute;left:-2px;width:46px;height:46px;border-radius:50%;background:#fff;border:2px solid var(--gold);display:flex;align-items:center;justify-content:center}
  .brands{position:absolute;left:500px;top:660px;width:275px;height:36px;background:var(--gold);color:var(--ink);font-size:15px;font-weight:700;line-height:36px;padding-left:16px}
  .cta{position:absolute;left:500px;top:706px;width:240px;color:var(--green);text-align:center}
  .cta .call{font-size:23px;font-weight:700;display:block;white-space:nowrap}
  .cta .free{font-size:96px;font-weight:900;color:var(--gold);display:block;line-height:.9;letter-spacing:1px}
  .cta .est{font-size:22px;font-weight:600;color:var(--ink);letter-spacing:9.5px;display:block;margin-top:2px}
  .phone-band{position:absolute;left:278px;top:869px;width:497px;height:42px;background:var(--green);border-radius:21px 0 0 21px;color:#fff;font-size:27px;font-weight:700;line-height:42px;padding-left:52px;letter-spacing:.3px}
  .phone-band .ph{position:absolute;left:6px;top:5px;width:32px;height:32px;border-radius:50%;background:#fff;display:flex;align-items:center;justify-content:center}
  .contact{position:absolute;top:925px;display:flex;align-items:center;gap:8px;font-size:23px;font-weight:700;color:var(--ink)}
</style>
</head>
<body>
<div class="canvas">
  <div class="flyer">
    <svg class="hero-art" width="775" height="1000" viewBox="0 0 775 1000" aria-hidden="false">
      <defs>
        <linearGradient id="dig" x1="0" y1="0" x2="1" y2="1">
          <stop offset="0" stop-color="#b79a74"/>
          <stop offset=".5" stop-color="#a58a66"/>
          <stop offset="1" stop-color="#d6d0c6"/>
        </linearGradient>
      </defs>
      <polygon points="440,0 775,0 775,420" fill="var(--gold)"/>
      <polygon points="0,265 455,265 430,345 0,345" fill="var(--green)"/>
      <ellipse cx="545" cy="218" rx="255" ry="172" transform="rotate(38 545 218)" fill="var(--green)"/>
      <ellipse cx="560" cy="205" rx="236" ry="160" transform="rotate(38 560 205)" fill="#fff"/>
      <ellipse cx="562" cy="203" rx="231" ry="155" transform="rotate(38 562 203)" fill="url(#dig)" role="img" aria-label="Photo of a plumber kneeling in a trench fitting white PVC drain pipe"/>
    </svg>

    <div class="brand"><span class="brand-dot"></span><span>HARLOW<br>MECHANICAL</span></div>

    <h1 class="headline"><span class="l1">GROWTH</span><span class="l2">THROUGH</span><span class="sub">COMMITMENT TO SERVICE</span></h1>
    <p class="intro">We are a HVAC, plumbing, and Controls contractor based out of West Michigan Serving the entire west side of the state.</p>

    <div class="attention">
      <span class="badge"><svg width="20" height="18" viewBox="0 0 20 18"><polygon points="10,1 19,17 1,17" fill="#f2c230"/><rect x="9" y="6" width="2" height="6" fill="#222"/><rect x="9" y="13.5" width="2" height="2" fill="#222"/></svg></span>
      <span class="word">ATTENTION!</span>
    </div>
    <p class="lead">WE ALSO PROVIDE THE FOLLOWING <em>PLUMBING SERVICES</em></p>

    <div class="service" style="left:35px;top:449px"><div class="thumb"><i role="img" aria-label="Lift station equipment" style="background:linear-gradient(135deg,#c9ccd0,#6f7479)"></i></div><div><h3>Lift <span>Stations</span></h3><p>Lorem Ipsum is simply dummy text of the</p></div></div>
    <div class="service" style="left:35px;top:515px"><div class="thumb g"><i role="img" aria-label="Stainless sink and faucet" style="background:linear-gradient(135deg,#9a9a98,#4d4d4c)"></i></div><div><h3>Sinks</h3><p>Lorem Ipsum is simply dummy text of the</p></div></div>
    <div class="service" style="left:35px;top:583px"><div class="thumb"><i role="img" aria-label="Worker in a confined space" style="background:radial-gradient(#5a6f88,#2b2118)"></i></div><div><h3>Confined <span>Space</span></h3><p>Lorem Ipsum is simply dummy text of the</p></div></div>
    <div class="service" style="left:35px;top:653px"><div class="thumb g"><i role="img" aria-label="Backflow prevention device" style="background:linear-gradient(135deg,#b8b3a4,#6b6a58)"></i></div><div><h3>Backflow<br><span>Prevention Devices</span></h3><small>(testing, installation, &amp; service)</small><p>Lorem Ipsum is simply dummy text of the</p></div></div>
    <div class="service" style="left:35px;top:720px"><div class="thumb"><i role="img" aria-label="Drinking fountain" style="background:linear-gradient(135deg,#e7b9a2,#9c9da0)"></i></div><div><h3>Drinking <span>Fountains</span></h3><p>Lorem Ipsum is simply dummy text of the</p></div></div>
    <div class="service" style="left:35px;top:788px"><div class="thumb g"><i role="img" aria-label="Roof drain" style="background:linear-gradient(135deg,#8d8f90,#3c3f42)"></i></div><div><h3>Roof <span>Drains</span></h3><p>Lorem Ipsum is simply dummy text of the</p></div></div>
    <div class="service" style="left:35px;top:858px"><div class="thumb"><i role="img" aria-label="Sump pumps" style="background:linear-gradient(135deg,#c4c6c8,#6e7276)"></i></div><div><h3>Sump <span>Pumps</span></h3><p>Lorem Ipsum is simply dummy text of the printing</p></div></div>

    <div class="service" style="left:271px;top:449px"><div class="thumb g"><i role="img" aria-label="Water main emergency repair" style="background:linear-gradient(135deg,#3d7fc0,#6a5232)"></i></div><div><h3>Water Main<br><span>Emergency Service</span></h3><p>Lorem Ipsum is simply dummy text of the</p></div></div>
    <div class="service" style="left:271px;top:514px"><div class="thumb g"><i role="img" aria-label="Toilets and urinals" style="background:linear-gradient(135deg,#e9ecee,#a7adb2)"></i></div><div><h3>Toilets / <span>Urinals</span></h3><p>Lorem Ipsum is simply dummy text of the</p></div></div>
    <div class="service" style="left:271px;top:583px"><div class="thumb"><i role="img" aria-label="Faucets and shower valves" style="background:linear-gradient(135deg,#cfd0cc,#63645f)"></i></div><div><h3>Faucets /<br><span>Shower Valves</span></h3><p>Lorem Ipsum is simply dummy text of the</p></div></div>
    <div class="service" style="left:271px;top:653px"><div class="thumb g"><i role="img" aria-label="Copper and steel piping" style="background:linear-gradient(135deg,#7c7f82,#2f3133)"></i></div><div><h3>Piping</h3><small>(copper, PVC, steel, PEX, galvanized)</small><p>Lorem Ipsum is simply dummy text of the</p></div></div>
    <div class="service" style="left:271px;top:720px"><div class="thumb g"><i role="img" aria-label="Water heaters" style="background:linear-gradient(135deg,#c8cacb,#73777a)"></i></div><div><h3>Water <span>Heaters</span></h3><p>Lorem Ipsum is simply dummy text of the</p></div></div>
    <div class="service" style="left:271px;top:787px"><div class="thumb g"><i role="img" aria-label="Floor and sink drains" style="background:linear-gradient(135deg,#c2a47c,#6d5a40)"></i></div><div><h3>Floor and<br><span>Sink Drains</span></h3><p>Lorem Ipsum is simply dummy text of the</p></div></div>

    <ul class="offer">
      <li style="top:18px"><span class="offer-icon" style="left:-56px;top:8px"><svg width="24" height="24" viewBox="0 0 24 24" fill="none" stroke="#333" stroke-width="1.5"><circle cx="12" cy="12" r="9"/><circle cx="12" cy="12" r="4"/></svg></span>NEW<br>INSTALLATIONS</li>
      <li style="top:82px"><span class="offer-icon" style="left:-56px;top:-12px"><svg width="24" height="24" viewBox="0 0 24 24" fill="none" stroke="#333" stroke-width="1.5"><rect x="5" y="11" width="14" height="9"/><path d="M9 11V6h6v5"/></svg></span>SERVICE</li>
      <li style="top:136px"><span class="offer-icon" style="left:-56px;top:-12px"><svg width="24" height="24" viewBox="0 0 24 24" fill="none" stroke="#333" stroke-width="1.5"><circle cx="14" cy="9" r="5"/><path d="M3 20h8l6-4"/></svg></span>MAINTENANCE</li>
    </ul>
    <div class="brands">ALL BRANDS OF EQUIPMENT</div>

    <div class="cta"><span class="call">CALL TODAY FOR A</span><span class="free">FREE</span><span class="est">ESTIMATION</span></div>

    <div class="phone-band"><span class="ph"><svg width="18" height="18" viewBox="0 0 24 24"><path d="M6.6 10.8a15 15 0 0 0 6.6 6.6l2.2-2.2a1 1 0 0 1 1-.25 11.4 11.4 0 0 0 3.6.57 1 1 0 0 1 1 1V20a1 1 0 0 1-1 1A17 17 0 0 1 3 4a1 1 0 0 1 1-1h3.5a1 1 0 0 1 1 1c0 1.25.2 2.45.57 3.6a1 1 0 0 1-.25 1z" fill="#111"/></svg></span>800-555-0142 / 616-555-0187</div>

    <div class="contact" style="left:44px"><svg width="26" height="18" viewBox="0 0 26 18"><rect x="1" y="1" width="24" height="16" fill="var(--gold)"/><path d="M1 1l12 9 12-9" stroke="#fff" stroke-width="1.6" fill="none"/></svg>ben@harlowind.com</div>
    <div class="contact" style="left:355px"><svg width="22" height="22" viewBox="0 0 22 22" fill="none" stroke="var(--gold)" stroke-width="1.8"><circle cx="11" cy="11" r="9"/><ellipse cx="11" cy="11" rx="4" ry="9"/><path d="M2 11h18M4 6h14M4 16h14"/></svg>www.harlowmechanical.com</div>
  </div>
</div>
</body>
</html>
```